Amber Ridge Partners Business Card

A business card design to accompany the logo design you completed on Pixel Forum. We are open to your proposals. I did add one idea below that might work, but we aren't married to the idea. The company is a real estate services company. Clientele are typically high net worth individuals, executive level employment or owners of their own company, 30-60 years old.

Our 1 (bad?) idea: double sided card; One side landscape with logo and word mark. Other side Portrait with the logo only (oversize watermark maybe?). Somewhere add text of Name (Marcus Tellingham), Title (Principal), phone # (555-214-7736) and email address (marcus@amberridgeco.example). There would be a second design with my wife's name, number and email in place of mine.

Again totally open to ideas here.

Industry/Entity Type

Real Estate

```html
<!DOCTYPE html>
<html lang="en">
<head>
<meta charset="utf-8">
<title>Amber Ridge Partners — Business Card</title>
<link rel="stylesheet" href="https://fonts.googleapis.com/css2?family=Cinzel:wght@400&family=Playfair+Display:ital,wght@1,700&family=Arimo:wght@400&display=swap">
<style>
  :root {
    --sage: #66925a;
    --band: #bbbfb9;
    --ink: #111111;
    --paper: #ffffff;
    --frame: #000000;
  }
  * { box-sizing: border-box; margin: 0; padding: 0; }
  html, body {
    width: 992px;
    height: 1200px;
    overflow: hidden;
    background: var(--paper);
  }
  .canvas {
    position: relative;
    width: 992px;
    height: 1200px;
  }
  .card {
    position: absolute;
    left: 127px;
    width: 737px;
    height: 433px;
    border: 3px solid var(--frame);
    border-radius: 5px;
    background: var(--paper);
    overflow: hidden;
  }
  .card--front { top: 89px; }
  .card--back { top: 653px; }
  .card__art {
    position: absolute;
    inset: 0;
    width: 100%;
    height: 100%;
  }
  .wordmark {
    position: absolute;
    left: 0;
    right: 0;
    top: 140px;
    height: 167px;
    display: flex;
    align-items: center;
    justify-content: center;
    gap: 22px;
  }
  .wordmark__mark {
    width: 34px;
    height: 34px;
    background: var(--sage);
  }
  .wordmark__name {
    font-family: "Cinzel", serif;
    font-weight: 400;
    font-size: 44px;
    color: var(--sage);
    letter-spacing: 1px;
  }
  .back-brand {
    position: absolute;
    right: 24px;
    top: 40px;
    width: 150px;
    font-family: "Cinzel", serif;
    font-weight: 400;
    font-size: 24px;
    line-height: 1.2;
    color: var(--sage);
    text-align: center;
  }
  .person {
    position: absolute;
    left: 31px;
    top: 88px;
  }
  .person__name {
    font-family: "Cinzel", serif;
    font-weight: 400;
    font-size: 28px;
    letter-spacing: 2px;
    color: var(--ink);
  }
  .person__title {
    margin: 2px 0 0 100px;
    font-family: "Playfair Display", serif;
    font-style: italic;
    font-weight: 700;
    font-size: 31px;
    color: var(--ink);
  }
  .contact {
    position: absolute;
    left: 0;
    right: 0;
    top: 302px;
    text-align: center;
    font-family: "Arimo", sans-serif;
    color: var(--ink);
  }
  .contact__phone { font-size: 28px; letter-spacing: 0.5px; }
  .contact__email {
    margin-top: 22px;
    font-size: 22px;
    letter-spacing: 0.5px;
    text-transform: uppercase;
  }
</style>
</head>
<body>
<main class="canvas">

  <section class="card card--front" aria-label="Card front">
    <svg class="card__art" viewBox="0 0 553 325" preserveAspectRatio="none" aria-hidden="true">
      <path class="swoosh" fill="var(--sage)"
            d="M10 11 C150 8, 290 22, 420 36 C480 40, 520 36, 545 33 C515 44, 470 47, 420 45 C290 32, 150 15, 10 11 Z"/>
      <rect class="band" x="0" y="105" width="553" height="125" fill="var(--band)"/>
      <path class="swoosh" fill="var(--sage)"
            d="M10 271 C150 264, 300 290, 420 304 C480 310, 520 300, 545 290 C520 304, 480 316, 420 314 C300 302, 150 274, 10 271 Z"/>
    </svg>
    <div class="wordmark">
      <span class="wordmark__mark" aria-hidden="true"></span>
      <span class="wordmark__name">Amber Ridge Partners</span>
    </div>
  </section>

  <section class="card card--back" aria-label="Card back">
    <svg class="card__art" viewBox="0 0 553 325" preserveAspectRatio="none" aria-hidden="true">
      <path class="stripe" fill="var(--sage)"
            d="M0 188 C120 178, 230 182, 330 186 C430 190, 500 182, 553 171 L553 180 C500 192, 430 199, 330 197 C230 195, 120 192, 0 200 Z"/>
      <path class="footer-field" fill="var(--sage)"
            d="M0 206 C120 199, 230 206, 330 212 C430 216, 500 208, 553 199 L553 325 L0 325 Z"/>
    </svg>
    <div class="back-brand">Amber Ridge Partners</div>
    <div class="person">
      <p class="person__name">Marcus Tellingham</p>
      <p class="person__title">Principal</p>
    </div>
    <div class="contact">
      <p class="contact__phone">555-214-7736</p>
      <p class="contact__email">marcus@amberridgeco.example</p>
    </div>
  </section>

</main>
</body>
</html>
```